KELVA GIFTS - Gift Card app

We have created an application to sell gift cards and greeting cards for Brindle Shop and Mervox Hub. Layout to remain the same, upgrade and change the graphics. Keep the background white. Must fit into existing app.

Logo design + 4 tutorial slides + 1 main page. The 5 current images are included and red box around what we want changed.

Pay particular attention to the red squares.

```html
<!DOCTYPE html>
<html lang="en">
<head>
<meta charset="UTF-8">
<title>KELVA GIFTS – Welcome</title>
<link rel="stylesheet" href="https://fonts.googleapis.com/css2?family=Montserrat:wght@600&display=swap">
<style>
  :root {
    --brand-red: #b3241f;
    --bg-white: #ffffff;
    --tone-blue: #7cc0e8;
    --tone-pink: #ee8aa0;
    --tone-orange: #e2a54a;
  }
  html, body {
    margin: 0;
    padding: 0;
    width: 1200px;
    height: 2596px;
    overflow: hidden;
    background: var(--bg-white);
  }
  .splash {
    position: relative;
    width: 1200px;
    height: 2596px;
    background: var(--bg-white);
  }
  .brand {
    position: absolute;
    top: 690px;
    left: 0;
    width: 1200px;
    text-align: center;
    font-family: 'Montserrat', sans-serif;
    font-weight: 600;
    color: var(--brand-red);
  }
  .brand-name {
    margin: 0;
    font-size: 190px;
    font-weight: 600;
    line-height: 1;
    letter-spacing: 3px;
  }
  .brand-tagline {
    margin: 180px 0 0;
    font-size: 78px;
    line-height: 1;
    letter-spacing: 92px;
    padding-left: 92px;
  }
  .gift-illustration {
    position: absolute;
    left: 0;
    bottom: 0;
    width: 1200px;
    height: 1116px;
    background: linear-gradient(180deg,
      var(--bg-white) 0%,
      var(--tone-blue) 40%,
      var(--tone-pink) 70%,
      var(--tone-orange) 100%);
  }
</style>
</head>
<body>
  <main class="splash">
    <div class="brand">
      <h1 class="brand-name">KELVA</h1>
      <p class="brand-tagline">GIFTS</p>
    </div>
    <div class="gift-illustration" role="img" aria-label="Illustration of a colourful pile of wrapped gift boxes with ribbons and bows, surrounded by small sparkles"></div>
  </main>
</body>
</html>
```